MOR

We need to design a power point presentation that can englobe all our company products.

This presentation has to have all the required to be used as template for future presentations.

We focus on prodcut developing for supermarkets, ( we help them with their own brand products ex. Sunny Pantry, KT, etc.)
Also we are on the marine industry, we develop ships and oil rigs for the Oil and deep water market.

Target Market(s)

Oil Companies
Supermarket companies
Retail Companies

Industry/Entity Type

It Company

Requirements
Must have
• Our Logo and company colors
Nice to have
• Something describing globalization.
Should not have
• Orange color

```html
<!DOCTYPE html>
<html lang="en">
<head>
<meta charset="utf-8">
<title>MOR – Presentation Title Slide</title>
<link rel="stylesheet" href="https://fonts.googleapis.com/css2?family=Orbitron:wght@700&family=Exo+2:wght@300&display=swap">
<style>
  :root {
    --paper: #ffffff;
    --navy: #2b3a9a;
    --sky: #1ba1e0;
    --leaf: #8cc63f;
    --mist-blue: rgba(214, 230, 244, 0.75);
    --mist-green: rgba(226, 238, 206, 0.6);
  }
  html, body {
    margin: 0;
    padding: 0;
    overflow: hidden;
    background: var(--paper);
  }
  .slide {
    position: relative;
    width: 1200px;
    height: 900px;
    overflow: hidden;
    background: var(--paper);
  }
  .backdrop-art {
    position: absolute;
    left: 0;
    top: 0;
    width: 520px;
    height: 867px;
    background:
      radial-gradient(ellipse 260px 460px at 190px 230px, var(--mist-blue) 0%, rgba(255,255,255,0) 100%),
      radial-gradient(ellipse 240px 380px at 300px 640px, var(--mist-green) 0%, rgba(255,255,255,0) 100%),
      radial-gradient(ellipse 200px 420px at 40px 560px, var(--mist-blue) 0%, rgba(255,255,255,0) 100%);
  }
  .brand {
    position: absolute;
    left: 196px;
    top: 424px;
    display: flex;
    align-items: center;
    gap: 16px;
  }
  .brand-dot {
    width: 34px;
    height: 34px;
    border-radius: 50%;
    background: var(--leaf);
  }
  .brand-name {
    margin: 0;
    font-family: "Exo 2", sans-serif;
    font-weight: 300;
    font-size: 60px;
    line-height: 1;
    letter-spacing: 4px;
    color: var(--sky);
  }
  .title-rule {
    position: absolute;
    left: 447px;
    top: 457px;
    width: 715px;
    height: 4px;
    background: var(--leaf);
  }
  .project-title {
    position: absolute;
    left: 684px;
    top: 408px;
    margin: 0;
    font-family: "Orbitron", sans-serif;
    font-weight: 700;
    font-size: 34px;
    letter-spacing: 2.3px;
    line-height: 1;
    color: var(--navy);
    white-space: nowrap;
  }
  .project-subtext {
    position: absolute;
    left: 684px;
    top: 472px;
    margin: 0;
    width: 500px;
    font-family: "Exo 2", sans-serif;
    font-weight: 300;
    font-size: 23px;
    line-height: 33px;
    letter-spacing: 1.5px;
    color: var(--sky);
    white-space: nowrap;
  }
  .footer-band {
    position: absolute;
    left: 0;
    bottom: 0;
    width: 1200px;
    height: 33px;
    background: var(--leaf);
  }
</style>
</head>
<body>
  <main class="slide">
    <div class="backdrop-art" role="img" aria-label="Faint sweeping ribbon decoration in pale blue and green"></div>

    <div class="brand">
      <span class="brand-dot"></span>
      <p class="brand-name">MOR</p>
    </div>

    <div class="title-rule"></div>
    <h1 class="project-title">PROJECT TITLE HERE</h1>
    <p class="project-subtext">Subtext here Subtext here Subtext here<br>Subtext here Subtext here Subtext here<br>Subtext here Subtext here</p>

    <div class="footer-band"></div>
  </main>
</body>
</html>
```